Medical Implant company needs a Top Quality Premium Brochure

We need to create a top quality brochure for VIP clients, formed by top spine surgeons. The main goal here is to cause a deep quality impact, positioning the company and it´s solutions above the others, with a refined, unique and creative material.

Special paper, hot stamping, innovative format are welcome.

For more information check out our website: www.velcorasurg.com.br (web translator are recommended for content understanding)

Velcorasurg works with top quality spine and pain management products, providing solutions for the medical specialists, investing in high quality processes and continued medical education.

Short briefing:
1 - Company profile
2 - Quality / vision
3 - Continued education programs
4 - Main products
5 - Main partners
6 - Final stuff (creative final thoughts / considerations)

FORMAT: 25 x 18,5 cm (horizontal)
PAGES - 16

REFERENCES:

https://www.portfoliqo.net/gallery/20417839/Medical-Healthcare-Profile-Brochure

https://www.portfoliqo.net/gallery/7162904/KT-Alpine-Style-Brochure

Target Market(s)

Mainly brazilian spine and neuro surgeons with minimally invasive surgery skills.

Industry/Entity Type

Education

Requirements
Must have

• 18 pages design

1. Cover
2. IMAGE + TITLE - About Us
3. IMAGE + TEXT - About Us
4. IMAGE + TITLE - Vision
5. IMAGE + TEXT - Vision
6. IMAGE + TITLE - Quality
7. IMAGE + TEXT - Quality
8. Timeline Left
9. Timeline Right
10. IMAGE + TITLE - Medical Education
11. IMAGE + TEXT - Medical Education
12. IMAGE + TITLE - Minimally Invasive Technology
13. IMAGE + TEXT - Minimally Invasive Technology
14. IMAGE + TITLE - Impact Phrase
15. IMAGE + TEXT - Impact Phrase
16. Back

As longs as the text is under development and will be placed internally in the winning design, please use 'lorem ipsum' for text areas. The titles can follow the index above.

Nice to have
• The use of office pictures with some style / artistic finish in pages "about us"

```html
<!DOCTYPE html>
<html lang="pt-BR">
<head>
<meta charset="utf-8">
<title>Velcorasurg – Qualidade</title>
<link href="https://fonts.googleapis.com/css2?family=Open+Sans:wght@400;600&family=Oswald:wght@700&display=swap" rel="stylesheet">
<style>
  :root {
    --backdrop: #b4b4b4;
    --paper: #e9eaea;
    --ink: #4a4d4f;
    --teal: #46aaa5;
    --teal-deep: #2f9a96;
    --slate: #5d6266;
    --white: #ffffff;
  }
  * { box-sizing: border-box; margin: 0; padding: 0; }
  html, body {
    width: 1200px; height: 856px; overflow: hidden;
    background: var(--backdrop);
    font-family: "Open Sans", Arial, sans-serif;
  }
  .spread {
    position: absolute; left: 40px; top: 221px;
    width: 1120px; height: 414px;
    display: flex;
    box-shadow: 0 10px 30px rgba(0,0,0,.25);
  }
  .page { position: relative; width: 560px; height: 414px; overflow: hidden; }

  /* left page */
  .page--text { background: var(--paper); }
  .page__swoosh { position: absolute; inset: 0; width: 100%; height: 100%; }
  .body-copy {
    position: absolute; left: 38px; top: 38px; width: 430px;
    color: var(--ink); font-size: 7.4px; line-height: 1.5;
  }
  .body-copy p + p { margin-top: 7px; }
  .mission-box {
    position: absolute; left: 250px; top: 262px; width: 255px; height: 100px;
    background: var(--teal-deep); color: var(--white);
    padding: 16px 18px; font-size: 7.6px; line-height: 1.55;
  }

  /* right page */
  .page--photo { background: var(--paper); }
  .photo {
    position: absolute; inset: 0;
    background:
      radial-gradient(ellipse at 70% 35%, #a77e66 0%, rgba(167,126,102,0) 35%),
      radial-gradient(ellipse at 75% 10%, #6a4d3a 0%, rgba(106,77,58,0) 45%),
      linear-gradient(160deg, #3f6f8f 0%, #2c5673 40%, #3b5f78 70%, #2d4a5e 100%);
  }
  .title-tab { position: absolute; left: 22px; top: 190px; width: 235px; height: 118px; }
  .title-tab__shadow {
    position: absolute; left: 14px; top: -10px; width: 235px; height: 108px;
    background: var(--slate);
  }
  .title-tab__block {
    position: absolute; left: 0; top: 0; width: 235px; height: 118px;
    background: var(--teal); opacity: .95;
    display: flex; align-items: center; justify-content: flex-end;
    padding-right: 28px;
  }
  .title-tab__text {
    font-family: "Oswald", "Arial Narrow", sans-serif; font-weight: 700;
    color: var(--white); font-size: 30px; line-height: 1.1;
    text-transform: uppercase; letter-spacing: .5px; text-align: left;
  }
</style>
</head>
<body>
<main class="spread">
  <section class="page page--text">
    <svg class="page__swoosh" viewBox="0 0 560 414" aria-hidden="true">
      <path d="M0 300 C 150 262, 330 228, 560 218 L 560 414 L 420 414 C 330 380, 160 360, 0 372 Z" fill="var(--teal)"/>
    </svg>
    <div class="body-copy">
      <p>A atenção com os processos desenvolvidos na empresa, bem como o cuidado na escolha dos produtos que comercializamos, são fatores que abrangem uma série de etapas de nossa política de qualidade, sendo nossos fornecedores certificados por padrões rigorosos, como o padrão ISO, a Marca CE e também as resoluções da agência sanitária nacional, que regulamentam e fornecem as diretrizes e orientações para o funcionamento da empresa. Do armazenamento até a comercialização, tudo é realizado com o máximo de cuidado e rigorosos padrões de qualidade, que são vistoriados e avaliados constantemente pela nossa equipe de profissionais.</p>
      <p>A política de qualidade da empresa engloba diversas etapas, desenvolvidas por nossos parceiros de negócios e fornecedores, ainda na produção, e pela Velcorasurg na distribuição dos produtos. A marca Velcorasurg envolvida no fornecimento de produtos para a saúde significa atenção total à qualidade e segurança.</p>
      <p>Somos mais fortes trabalhando juntos pela excelência, construindo nosso diferencial com dedicação, paixão e comprometimento de cada colaborador. É por isto que, a cada procedimento com a marca Velcorasurg, não implantamos produtos, implantamos qualidade.</p>
      <p>Clique aqui para conhecer as principais etapas do nosso sistema de qualidade.</p>
    </div>
    <div class="mission-box">
      Ir ao encontro das necessidades de nossos clientes, superando expectativas, com produtos desenvolvidos sob rigorosos padrões de qualidade, realizando nossas atividades com foco no bem-estar dos profissionais da saúde, seus pacientes e toda a cadeia produtiva envolvida em nosso seguimento de atuação.
    </div>
  </section>

  <section class="page page--photo">
    <div class="photo" role="img" aria-label="Photo: a nurse in blue scrubs with a stethoscope holding a patient's hands in comfort"></div>
    <div class="title-tab">
      <div class="title-tab__shadow"></div>
      <div class="title-tab__block">
        <h2 class="title-tab__text">Impact<br>Phrase</h2>
      </div>
    </div>
  </section>
</main>
</body>
</html>
```